Tavrin Telecom Corporate Website & Social Branding

We are looking for a new website for our startup telecom which provides UCaaS, SD-WAN, Business SMS/MMS, Video Conferencing, Managed Network Service & more.

Target Market(s)

Small offices from 1-250 users

Industry/Entity Type

Telecomunications

Coding

Coded - Design and coding required

Colors
0054AA
0677BA
7BADD7
CADEEF
E8F1F8

```html
<!DOCTYPE html>
<html lang="en">
<head>
<meta charset="utf-8">
<title>Tavrin Telecom — Meeting doesn't get any easier</title>
<link href="https://fonts.googleapis.com/css2?family=Poppins:wght@400;500;600;700;800&display=swap" rel="stylesheet">
<style>
:root{
  --navy:#0054AA;
  --blue:#0677BA;
  --bright:#1289D0;
  --sky:#7BADD7;
  --pale:#CADEEF;
  --mist:#E8F1F8;
  --ink:#1f1f1f;
  --text:#555;
  --muted:#8a8a8a;
  --panel:#efefef;
  --line:#e2e2e2;
  --dark:#232323;
  --star:#f5b300;
}
*{box-sizing:border-box;margin:0;padding:0}
html,body{width:1200px;height:4243px;overflow:hidden}
body{position:relative;background:#fff;font-family:'Poppins',sans-serif;color:var(--ink)}
.abs{position:absolute}
a{color:inherit;text-decoration:none}

/* brand */
.brand{display:flex;align-items:center;gap:10px;font-weight:700;font-size:30px;letter-spacing:-.5px;color:var(--navy);white-space:nowrap}
.brand .dot{width:38px;height:38px;border-radius:50%;background:var(--blue)}

/* header */
.topbar{top:10px;right:90px;display:flex;gap:26px;font-size:11px;font-weight:500;color:#333;align-items:center}
.topbar .sep{width:1px;height:16px;background:#ccc}
.mainnav{top:66px;left:398px;display:flex;gap:30px;font-size:12.5px;font-weight:500;color:#333;align-items:center}
.mainnav span::after{content:" ▾";font-size:9px}
.btn-demo{background:#ececec;border-radius:20px;padding:10px 26px;font-weight:700;font-size:12px;color:#222}

/* hero */
.hero-title{top:202px;left:88px;font-size:58px;font-weight:800;line-height:1.07;letter-spacing:-1px}
.hero-sub{top:346px;left:88px;font-size:14px;color:#444}
.btn{display:inline-block;background:var(--bright);color:#fff;font-weight:700;font-size:11.5px;border-radius:20px;padding:11px 24px}
.link-u{font-weight:700;font-size:11.5px;border-bottom:1.5px solid #222;padding-bottom:2px}
.art{border-radius:8px}

.band{top:0;left:0;width:1200px;height:1128px}
.ratings{top:860px;left:257px;display:grid;grid-template-columns:repeat(3,217px);gap:17px 18px}
.rcard{height:86px;background:#fff;border-radius:6px;display:flex;flex-direction:column;align-items:center;justify-content:center;gap:8px;box-shadow:0 4px 14px rgba(0,0,0,.08)}
.rcard .mark{width:70px;height:16px;border-radius:4px;background:var(--pale)}
.rcard .score{font-size:14px;font-weight:700;display:flex;gap:6px;align-items:center}
.stars{color:var(--star);letter-spacing:1px}

/* specialize */
.h2{font-size:36px;font-weight:700;text-align:center;width:1200px;left:0}
.hub-ring{left:436px;top:1297px;width:330px;height:330px;border-radius:50%;background:#f4f4f4;box-shadow:0 0 0 2px #ececec}
.hub{left:466px;top:1327px;width:270px;height:270px;border-radius:50%;background:#fff;box-shadow:0 6px 24px rgba(0,0,0,.08);display:flex;align-items:center;justify-content:center}
.hub .brand{font-size:24px}
.spec{width:260px;font-size:11.5px;color:var(--muted);line-height:1.65}
.spec h3{font-size:13.5px;font-weight:700;color:var(--ink);margin-bottom:4px}
.spec.left{text-align:right}
.icon-dot{width:66px;height:66px;border-radius:50%;background:#fff;box-shadow:0 4px 14px rgba(0,0,0,.1);display:flex;align-items:center;justify-content:center}

/* remote panel */
.remote{left:89px;top:1725px;width:1022px;height:328px;background:var(--panel);border-radius:16px}

.feature{text-align:center;width:220px;font-size:13.5px;font-weight:600}
.feature svg{display:block;margin:0 auto 12px}
.divider{height:1px;background:var(--line)}

/* empower */
.emp-title{top:2360px;left:88px;font-size:36px;font-weight:700;line-height:1.12}
.emp-text{top:2505px;left:92px;width:378px;font-size:13.5px;color:var(--text);line-height:1.75}

/* testimonials */
.sub{font-size:16px;font-weight:600;text-align:center;width:1200px;left:0}
.tcard{top:2922px;width:327px;height:197px;background:#fff;border-radius:6px;box-shadow:0 4px 22px rgba(0,0,0,.08);padding:58px 24px 0}
.tcard .quote{position:absolute;right:60px;top:8px;font-size:90px;color:#e6e6e6;font-weight:800;line-height:1}
.tcard p{position:relative;font-size:13px;color:#444;line-height:1.7}
.tcard .who{position:absolute;left:24px;right:24px;bottom:22px;display:flex;justify-content:space-between;font-size:13px;font-weight:700}
.tcard .stars{font-size:13px}
.avatar{width:72px;height:72px;border-radius:50%;background:linear-gradient(135deg,#b9876a,#6d4b3a);top:-36px;left:36px;border:3px solid #fff}

.integ{top:3218px;font-size:23px;font-weight:700;line-height:1.42;text-align:center;width:1200px;left:0}
.partner{top:3294px;width:150px;height:150px;border-radius:50%;background:#ececec;display:flex;align-items:center;justify-content:center;gap:6px;font-weight:700;font-size:15px;color:#3a3a3a}
.partner i{width:14px;height:14px;background:#3a3a3a;display:block}

/* cta */
.cta{left:135px;top:3519px;width:932px;height:155px;border-radius:78px;background:var(--bright);z-index:2}
.cta h2{position:absolute;left:66px;top:36px;color:#fff;font-size:36px;font-weight:700;line-height:1.22}
.cta .btn-w{position:absolute;left:698px;top:55px;background:#fff;color:#1a1a1a;font-weight:700;font-size:14px;border-radius:24px;padding:13px 28px}

/* footer */
.footer-bg{left:0;top:3600px;width:1200px;height:643px}
.social{top:3772px;width:44px;height:44px;border-radius:50%;background:#3a3a3a;display:flex;align-items:center;justify-content:center}
.social i{width:14px;height:14px;border-radius:50%;background:#fff;display:block}
.fcol{top:3920px;color:#fff}
.fcol h4{font-size:15px;font-weight:700;margin-bottom:14px}
.fcol li{list-style:none;font-size:11.5px;color:#ddd;line-height:22px}
.legal{top:4205px;left:0;width:1200px;padding:0 89px;display:flex;justify-content:space-between;font-size:11px;color:#ddd}
.legal nav{display:flex;gap:22px}
.chat{left:1133px;top:4162px;width:44px;height:44px;border-radius:50%;background:var(--bright);display:flex;align-items:center;justify-content:center}
</style>
</head>
<body>

<!-- hero band -->
<svg class="abs band" viewBox="0 0 1200 1128" aria-hidden="true">
  <defs>
    <linearGradient id="bandFill" x1="0" y1="0" x2="1" y2="1">
      <stop offset="0" stop-color="#1a8fd6"/><stop offset="1" stop-color="#0a7bc4"/>
    </linearGradient>
  </defs>
  <path d="M0 680 C120 600 230 540 360 560 C520 585 600 700 780 735 C950 765 1080 700 1200 620 L1200 1128 L0 1128 Z" fill="url(#bandFill)"/>
  <path d="M700 720 C880 780 1050 740 1200 640 L1200 700 C1060 800 880 810 700 720 Z" fill="#fff" opacity=".9"/>
  <circle cx="1080" cy="720" r="160" fill="#ffffff" opacity=".12"/>
  <circle cx="1080" cy="720" r="110" fill="#0d6aa6" opacity=".25"/>
</svg>
<div class="abs" role="img" aria-label="Decorative striped circle" style="left:180px;top:560px;width:255px;height:200px;border-radius:0 0 130px 130px;background:#7fc0ea;opacity:.55"></div>

<!-- header -->
<div class="abs brand" style="left:88px;top:30px"><span class="dot"></span>Tavrin Telecom</div>
<div class="abs topbar"><span>JOIN A MEETING</span><span>SUPPORT</span><span>LOGIN ▾</span><span class="sep"></span>
  <svg width="12" height="12" viewBox="0 0 12 12"><circle cx="5" cy="5" r="3.8" fill="none" stroke="#333" stroke-width="1.6"/><path d="M8 8l3 3" stroke="#333" stroke-width="1.6"/></svg>
</div>
<nav class="abs mainnav"><span>PRODUCTS</span><span>SOLUTIONS</span><span>PLANS &amp; PRICING</span><span>PARTNERS</span><span>RESOURCES</span><a class="btn-demo">VIEW DEMO</a></nav>

<h1 class="abs hero-title">Meeting doesn't<br>get any easier</h1>
<p class="abs hero-sub">Gather your team and get work done, no matter where you are.</p>
<div class="abs" style="top:388px;left:88px;display:flex;gap:18px;align-items:center"><a class="btn">SEE PRICING</a><a class="link-u">CONTACT US</a></div>

<div class="abs art" role="img" aria-label="Illustration of two women waving on a video call, with a potted plant" style="left:612px;top:150px;width:500px;height:486px;background:radial-gradient(circle at 30% 30%,#f2f2f2 0 38%,transparent 39%),linear-gradient(180deg,#f7f7f7,#e9eef3);"></div>

<div class="abs ratings">
  <div class="rcard"><span class="mark"></span><span class="score">4.5 <span class="stars">★★★★★</span></span></div>
  <div class="rcard"><span class="mark"></span><span class="score">4.7 <span class="stars">★★★★★</span></span></div>
  <div class="rcard"><span class="mark"></span><span class="score">5.0 <span class="stars">★★★★★</span></span></div>
  <div class="rcard"><span class="mark"></span><span class="score">4.7 <span class="stars">★★★★★</span></span></div>
  <div class="rcard"><span class="mark"></span><span class="score">5.0 <span class="stars">★★★★★</span></span></div>
  <div class="rcard"><span class="mark"></span><span class="score">4.7 <span class="stars">★★★★★</span></span></div>
</div>

<!-- specialize -->
<h2 class="abs h2" style="top:1205px">We specialize in</h2>
<div class="abs hub-ring"></div>
<div class="abs hub"><div class="brand"><span class="dot" style="width:28px;height:28px"></span>Tavrin Telecom</div></div>

<div class="abs spec left" style="left:133px;top:1292px"><h3>UCaaS</h3>Aenean sollicitudinlorem quis bibendum nisi auctor nisi elit consequat ipsum.</div>
<div class="abs spec left" style="left:80px;top:1414px"><h3>SD-WAN</h3>Aenean sollicitudinlorem quis bibendum nisi auctor nisi elit consequat ipsum.</div>
<div class="abs spec left" style="left:125px;top:1539px"><h3>Business SMS/MMS</h3>Aenean sollicitudinlorem quis bibendum nisi auctor nisi elit consequat ipsum.</div>
<div class="abs spec" style="left:810px;top:1292px"><h3>Video Conferencing</h3>Aenean sollicitudinlorem quis bibendum nisi auctor nisi elit consequat ipsum.</div>
<div class="abs spec" style="left:856px;top:1414px"><h3>Managed Network</h3>Aenean sollicitudinlorem quis bibendum nisi auctor nisi elit consequat ipsum.</div>
<div class="abs spec" style="left:828px;top:1539px"><h3>Real-time analytics</h3>Aenean sollicitudinlorem quis bibendum nisi auctor nisi elit consequat ipsum.</div>

<div class="abs icon-dot" style="left:415px;top:1297px"><svg width="32" height="32" viewBox="0 0 32 32" fill="none" stroke="#0677BA" stroke-width="1.6"><rect x="4" y="6" width="24" height="15" rx="2"/><path d="M12 26h8M16 21v5"/><circle cx="16" cy="13" r="3"/></svg></div>
<div class="abs icon-dot" style="left:374px;top:1416px"><svg width="32" height="32" viewBox="0 0 32 32" fill="none" stroke="#0677BA" stroke-width="1.6"><circle cx="16" cy="16" r="10"/><path d="M6 16h20M16 6c4 4 4 16 0 20M16 6c-4 4-4 16 0 20"/></svg></div>
<div class="abs icon-dot" style="left:400px;top:1536px"><svg width="32" height="32" viewBox="0 0 32 32" fill="none" stroke="#0677BA" stroke-width="1.6"><rect x="9" y="4" width="14" height="24" rx="2"/><path d="M14 24h4M12 10h8M12 14h6"/></svg></div>
<div class="abs icon-dot" style="left:719px;top:1297px"><svg width="32" height="32" viewBox="0 0 32 32" fill="none" stroke="#0677BA" stroke-width="1.6"><rect x="4" y="6" width="24" height="17" rx="2"/><path d="M4 19h24M12 27h8"/><circle cx="12" cy="12" r="2"/><circle cx="20" cy="12" r="2"/></svg></div>
<div class="abs icon-dot" style="left:764px;top:1416px"><svg width="32" height="32" viewBox="0 0 32 32" fill="none" stroke="#0677BA" stroke-width="1.6"><circle cx="16" cy="16" r="4"/><circle cx="16" cy="5" r="2.5"/><circle cx="16" cy="27" r="2.5"/><circle cx="6" cy="11" r="2.5"/><circle cx="26" cy="11" r="2.5"/><circle cx="6" cy="21" r="2.5"/><circle cx="26" cy="21" r="2.5"/><path d="M16 8v4M16 20v4M8 12l5 2M24 12l-5 2M8 20l5-2M24 20l-5-2"/></svg></div>
<div class="abs icon-dot" style="left:732px;top:1536px"><svg width="32" height="32" viewBox="0 0 32 32" fill="none" stroke="#0677BA" stroke-width="1.6"><rect x="5" y="5" width="22" height="18" rx="2"/><circle cx="16" cy="14" r="5"/><path d="M16 9v5h5M12 27h8"/></svg></div>

<!-- remote work -->
<div class="abs remote"></div>
<div class="abs art" role="img" aria-label="Illustration of a woman with a headset working at a laptop desk beside a plant" style="left:123px;top:1646px;width:445px;height:370px;background:linear-gradient(180deg,rgba(123,173,215,0) 0%,rgba(123,173,215,.3) 100%)"></div>
<h2 class="abs" style="top:1803px;left:585px;font-size:31px;font-weight:700;line-height:1.27;width:520px">Empowering remote work in a unified &amp; secure environment. As it should be.</h2>
<a class="abs btn" style="left:586px;top:1951px">SWITCH ME</a>

<div class="abs feature" style="left:254px;top:2110px"><svg width="64" height="64" viewBox="0 0 64 64" fill="none" stroke="#0677BA" stroke-width="2"><circle cx="26" cy="22" r="8"/><circle cx="26" cy="22" r="15" stroke-dasharray="3 3"/><path d="M26 22v20l6-4 5 10 4-2-5-10h8z"/></svg>Start in a click</div>
<div class="abs feature" style="left:455px;top:2110px"><svg width="64" height="64" viewBox="0 0 64 64" fill="none" stroke="#0677BA" stroke-width="2"><rect x="10" y="14" width="44" height="32" rx="3"/><path d="M22 54h20M32 46v8M28 24l10 6-10 6z"/><path d="M26 8c4-3 8-3 12 0"/></svg>HD Voice and Video</div>
<div class="abs feature" style="left:683px;top:2110px"><svg width="64" height="64" viewBox="0 0 64 64" fill="none" stroke="#0677BA" stroke-width="2"><rect x="24" y="28" width="16" height="14" rx="2"/><path d="M27 28v-5a5 5 0 0110 0v5M6 20h14M6 44h14M44 20h14M44 44h14M20 20l4 8M20 44l4-4M44 20l-4 8M44 44l-4-4"/><circle cx="6" cy="20" r="3"/><circle cx="6" cy="44" r="3"/><circle cx="58" cy="20" r="3"/><circle cx="58" cy="44" r="3"/></svg>Enterprise Grade Security</div>

<div class="abs divider" style="left:89px;top:2275px;width:1022px"></div>

<!-- empower -->
<h2 class="abs emp-title">Empower<br>every employee<br>globally</h2>
<p class="abs emp-text">If everybody is responsible for customer experience, you'd better give everybody the capabilities they need to be successful, from the front desk to the contact center and beyond. Equip every role across the organization with cloud communications by Vantel.</p>
<a class="abs btn" style="left:90px;top:2643px;padding:11px 26px">READ MORE</a>
<div class="abs art" role="img" aria-label="World map illustration with location pins and people chatting on phones" style="left:527px;top:2345px;width:584px;height:363px;background:radial-gradient(ellipse at 50% 50%,#eef2f6 0 55%,#fff 75%)"></div>

<!-- testimonials -->
<h2 class="abs h2" style="top:2781px">Don't take our word for it...</h2>
<p class="abs sub" style="top:2830px">We're Trusted by over 6,000 customers</p>

<div class="abs tcard" style="left:89px"><div class="abs avatar" role="img" aria-label="Customer portrait"></div><span class="quote">“</span><p>Aenean sollicitudin, lorem quis bibendum auctor, nisi elit consequat ipsum sagittis sem nibh id elit duis sed odio.</p><div class="who"><span>Mira Delacourt</span><span class="stars">★★★★★</span></div></div>
<div class="abs tcard" style="left:433px"><div class="abs avatar" role="img" aria-label="Customer portrait" style="background:linear-gradient(135deg,#6d7f8a,#2e3a40)"></div><span class="quote">“</span><p>Aenean sollicitudin, lorem quis bibendum auctor, nisi elit consequat ipsum sagittis sem nibh id elit duis sed odio.</p><div class="who"><span>Jonah Whitfield</span><span class="stars">★★★★★</span></div></div>
<div class="abs tcard" style="left:778px"><div class="abs avatar" role="img" aria-label="Customer portrait" style="background:linear-gradient(135deg,#a08a7c,#5a4a42)"></div><span class="quote">“</span><p>Aenean sollicitudin, lorem quis bibendum auctor, nisi elit consequat ipsum sagittis sem nibh id elit duis sed odio.</p><div class="who"><span>Elian Brooks</span><span class="stars">★★★★★</span></div></div>

<h2 class="abs integ">An open integration framework that<br>accelerates every workflow</h2>
<div class="abs partner" style="left:188px"><i></i>Nolvex</div>
<div class="abs partner" style="left:356px">Brightway</div>
<div class="abs partner" style="left:526px"><i></i>Lumora</div>
<div class="abs partner" style="left:695px">Kestrel</div>
<div class="abs partner" style="left:863px">Pureloop</div>

<!-- cta -->
<div class="abs cta"><h2>Bring everyone and everything<br>together on Tavrin Telecom</h2><a class="btn-w">SEE PRICING</a></div>

<!-- footer -->
<svg class="abs footer-bg" viewBox="0 0 1200 643" aria-hidden="true">
  <path d="M0 40 C300 140 900 140 1200 0 L1200 643 L0 643 Z" fill="#232323"/>
</svg>
<div class="abs brand" style="left:496px;top:3772px;color:#fff"><span class="dot" style="background:#fff"></span>Tavrin Telecom</div>
<div class="abs social" style="left:911px"><i></i></div>
<div class="abs social" style="left:962px"><i></i></div>
<div class="abs social" style="left:1015px"><i></i></div>
<div class="abs social" style="left:1066px"><i></i></div>
<div class="abs divider" style="left:89px;top:3876px;width:1022px;background:#3d3d3d"></div>

<div class="abs fcol" style="left:89px"><h4>Open Ecosystem</h4><ul><li>Developer platform</li><li>APIs</li><li>Integrated apps</li><li>App gallery</li><li>Developer support</li><li>Developer community</li><li>Games and rewards</li></ul></div>
<div class="abs fcol" style="left:326px"><h4>Partners</h4><ul><li>Global service providers</li><li>Channel partners</li><li>ISV partners</li><li>Connectivity partners</li><li>Affiliate partners</li><li>Strategic alliances</li><li>Partner portal</li></ul></div>
<div class="abs fcol" style="left:551px"><h4>Resources</h4><ul><li>Resource center</li><li>Blog</li><li>Customer stories</li><li>Newsroom</li><li>Product demos</li><li>Product releases</li><li>Product Accessibility</li><li>Events</li></ul></div>
<div class="abs fcol" style="left:760px"><h4>About Us</h4><ul><li>Our company</li><li>Leadership</li><li>Awards</li><li>Investor relations</li><li>Ventures</li><li>Trust Center</li><li>Corporate Responsibility</li><li>Diversity and Inclusion</li></ul></div>
<div class="abs fcol" style="left:979px"><h4>Quick Links</h4><ul><li>App Download</li><li>Join a meeting</li><li>Corvale App Login</li><li>Admin Portal Login</li><li>Careers</li><li>Support</li><li>Contact Sales</li></ul></div>

<div class="abs divider" style="left:89px;top:4186px;width:1022px;background:#3d3d3d"></div>
<div class="abs legal"><span>© 2022 Tavrin Telecom, All rights reserved.</span><nav><span>Legal</span><span>Privacy Notice</span><span>Cookie Preferences</span><span>Site Map</span><span>Accessibility</span><span>Contact Us</span></nav></div>
<div class="abs chat"><svg width="22" height="20" viewBox="0 0 22 20"><path d="M11 2C6 2 2 5 2 9c0 2 1 4 3 5l-1 4 4-2c1 .3 2 .4 3 .4 5 0 9-3 9-7.4S16 2 11 2z" fill="#fff"/><circle cx="7" cy="9" r="1.2" fill="#1289D0"/><circle cx="11" cy="9" r="1.2" fill="#1289D0"/><circle cx="15" cy="9" r="1.2" fill="#1289D0"/></svg></div>

</body>
</html>
```